Statement on the current financial and economic crisis, with a focus on Greece,

Anybody can become angry - that is easy, but to be angry with the right person and to the right degree and at the right time and for the right purpose, and in the right way - that is not within everybody's power and is not easy.
(Thessidor ) greek philosopher

i want to do a poster with this words from Thessidor greek philosopher and to show this statement for the greek people... its about for my project that i am doing.
Updates

Target Market(s)

my audience will be greek people but not only, from 18-80 years old for that reason i want my statement to be in english.

Industry/Entity Type

Financial

Requirements
Must have
• Anybody can become angry - that is easy, but to be angry with the right person and to the right degree and at the right time and for the right purpose, and in the right way - that is not within everybody's power and is not easy.
i want to show in my poster this statement from:
Thessidor greek philosopher (384 – 322 BC)

```html
<!DOCTYPE html>
<html lang="en">
<head>
<meta charset="utf-8">
<title>Thessidor – Statement Poster</title>
<link rel="stylesheet" href="https://fonts.googleapis.com/css2?family=Bitter:wght@700&display=swap">
<style>
  :root {
    --page: #ffffff;
    --poster-blue: #0388d2;
    --poster-glow: #4fb0e6;
    --text-white: #ffffff;
    --accent-yellow: #f7c600;
  }
  html, body {
    margin: 0;
    padding: 0;
    width: 900px;
    height: 1200px;
    overflow: hidden;
    background: var(--page);
  }
  .canvas {
    position: relative;
    width: 900px;
    height: 1200px;
    background: var(--page);
  }
  .poster {
    position: absolute;
    left: 96px;
    top: 100px;
    width: 707px;
    height: 1000px;
    background: radial-gradient(circle at 48% 21%, var(--poster-glow) 0%, var(--poster-blue) 38%, var(--poster-blue) 100%);
    font-family: "Bitter", "Georgia", serif;
    font-weight: 700;
    color: var(--text-white);
  }
  .quote-mark {
    position: absolute;
    fill: var(--text-white);
  }
  .quote-mark--open {
    left: 62px;
    top: 56px;
  }
  .quote-mark--close {
    left: 542px;
    top: 712px;
  }
  .statement {
    position: absolute;
    left: 60px;
    top: 170px;
    margin: 0;
    font-size: 41px;
    line-height: 65.8px;
    letter-spacing: 0.2px;
    white-space: nowrap;
  }
  .statement__highlight {
    color: var(--accent-yellow);
  }
  .attribution {
    position: absolute;
    right: 59px;
    top: 842px;
    margin: 0;
    text-align: right;
    font-size: 27px;
    line-height: 40px;
  }
</style>
</head>
<body>
<div class="canvas">
  <section class="poster">
    <svg class="quote-mark quote-mark--open" width="110" height="86" viewBox="0 0 110 86" aria-hidden="true">
      <path d="M45 2 C22 9 4 24 2 46 L2 82 L45 82 L45 40 L25 40 C27 27 34 19 45 15 Z"/>
      <path d="M107 2 C84 9 66 24 64 46 L64 82 L107 82 L107 40 L87 40 C89 27 96 19 107 15 Z"/>
    </svg>

    <p class="statement">Anybody can become angry<br>– that is easy, but to be<br>angry with the right person<br>and to the right degree and<br>at the right time and for the<br>right purpose, and in the<br>right way – <span class="statement__highlight">that is not</span><br><span class="statement__highlight">within everybody's power</span><br><span class="statement__highlight">and is not easy.</span></p>

    <svg class="quote-mark quote-mark--close" width="110" height="86" viewBox="0 0 110 86" aria-hidden="true">
      <path d="M2 84 C25 77 43 62 45 40 L45 2 L2 2 L2 44 L22 44 C20 57 13 65 2 69 Z"/>
      <path d="M64 84 C87 77 105 62 107 40 L107 2 L64 2 L64 44 L84 44 C82 57 75 65 64 69 Z"/>
    </svg>

    <p class="attribution">Thessidor<br>Greek philosopher (384 – 322 BC)</p>
  </section>
</div>
</body>
</html>
```